2nd Generation Blind Manufacturer & Retailer Needs A Stationary Set

We need a stationary set for a family business located the in the Whitsundays (QLD). We retail and manufacture blinds awnings and shutters. Second generation, in operation for over 30 years.

Final draft must include at minimum:

Business Card (2 Sided)
Letterhead
Presentation Folder

Target Market(s)

home owners, landlords, builders, real estate agents, shopping centres

Industry/Entity Type

Textile

Requirements
Must have
• Design needs to work in mono as well as colour print
Nice to have
• Relevant to the textile industry
Should not have
• The inclusion of blinds, awnings or shutters is an automatic no-no

```html
<!DOCTYPE html>
<html lang="en">
<head>
<meta charset="utf-8">
<title>Bayline Blinds – Stationery Set</title>
<link href="https://fonts.googleapis.com/css2?family=Cinzel:wght@400&family=Arimo:wght@400;700&family=Noto+Serif:wght@400;700&display=swap" rel="stylesheet">
<style>
:root{
  --backdrop:#e4e4e6;
  --paper:#ffffff;
  --slate:#6b6b6b;
  --slate-dark:#636363;
  --ink:#1d1d1d;
  --muted:#6f6f6f;
  --yellow:#f6e726;
  --red:#ea2229;
  --plum:#7b2a83;
  --white:#ffffff;
}
*{box-sizing:border-box;margin:0;padding:0}
html,body{width:1189px;height:1200px;overflow:hidden;background:var(--backdrop)}
body{position:relative;font-family:"Arimo",Arial,sans-serif;color:var(--ink)}
.sheet{position:absolute;overflow:hidden}

/* wordmark */
.brand{position:absolute;display:flex;align-items:center}
.brand-square{width:48px;height:48px;background:var(--slate)}
.brand-rule{width:1px;height:74px;background:var(--slate);margin:0 9px}
.brand-name{font-family:"Cinzel",serif;font-weight:400;color:var(--slate);font-size:27px;line-height:23px;letter-spacing:1px}
.brand.on-dark .brand-square{background:var(--white)}
.brand.on-dark .brand-rule{background:var(--white)}
.brand.on-dark .brand-name{color:var(--white)}
.brand.small .brand-square{width:38px;height:38px}
.brand.small .brand-rule{height:56px;margin:0 7px}
.brand.small .brand-name{font-size:22px;line-height:18px}

/* letterhead */
.letterhead{left:72px;top:100px;width:508px;height:657px;background:var(--paper)}
.letterhead .brand{left:48px;top:45px}
.lh-contact{position:absolute;right:46px;top:55px;text-align:right;font-size:9px;line-height:10.5px;color:var(--muted)}
.lh-contact .gap{height:6px}
.icon{display:inline-block;width:7px;height:7px;background:var(--plum);border-radius:1px;margin-left:4px;vertical-align:-1px}
.recipient{position:absolute;left:48px;top:187px;font-size:8.5px;line-height:10px}
.recipient .recipient-name{display:block;font-size:10px;margin-bottom:4px;font-weight:700}
.body-copy{position:absolute;left:48px;top:253px;width:396px;font-size:9.3px;line-height:15px;text-align:left;letter-spacing:-.15px}
.body-copy p+p{margin-top:15px}
.closing{position:absolute;left:48px;top:512px;font-size:9px}
.signature{position:absolute;left:46px;top:530px;width:120px;height:38px;background:linear-gradient(90deg,#e9e9e9,#f6f6f6);border-radius:3px}
.signoff{position:absolute;left:48px;top:575px;font-size:9.5px;line-height:11.5px}
.signoff .signer{font-weight:700}
.bands{position:absolute;left:0;bottom:0;width:100%}
.letterhead .bands{height:74px}

/* folder */
.folder{left:610px;top:100px;width:506px;height:653px;background:var(--slate)}
.folder-spine{position:absolute;left:26px;top:0;width:2px;height:100%;background:var(--slate-dark);box-shadow:1px 0 0 #777}
.folder .brand{left:150px;top:166px}
.folder-url{position:absolute;left:0;width:100%;top:600px;text-align:center;font-family:"Noto Serif",serif;font-size:8px;color:var(--white);letter-spacing:.3px}

/* business cards */
.card-front{left:150px;top:860px;width:351px;height:200px;background:var(--paper)}
.card-front .brand{left:19px;top:67px}
.card-divider{position:absolute;left:187px;top:32px;width:1px;height:124px;background:#9a9a9a}
.card-details{position:absolute;left:199px;top:39px;font-family:"Noto Serif",serif;color:var(--muted);font-size:10px;line-height:12.2px}
.card-details .person{font-size:13px;font-weight:700;color:var(--slate);line-height:14px}
.card-details .role{color:var(--plum);font-size:10px;margin-bottom:12px}
.card-details .addr{margin-bottom:6px}
.card-details .icon{margin:0 4px 0 0;width:9px;height:9px;vertical-align:-1px}
.card-front .bands{height:40px}
.card-back{left:687px;top:860px;width:351px;height:200px;background:var(--slate)}
.card-back .brand{left:85px;top:60px}
.card-url{position:absolute;left:0;width:100%;top:145px;text-align:center;font-family:"Noto Serif",serif;font-size:10px;color:var(--white)}
</style>
</head>
<body>

<section class="sheet letterhead" aria-label="Letterhead">
  <div class="brand">
    <span class="brand-square"></span><span class="brand-rule"></span>
    <span class="brand-name">Bayline<br>Blinds</span>
  </div>
  <div class="lh-contact">
    0000 Youe Address,2nd Ste.<br>Harbourton, Westland 1234
    <div class="gap"></div>
    123 456 7890<span class="icon"></span><br>
    your@yourcompany.com<span class="icon"></span><br>
    www.yourcompany.com<span class="icon"></span>
  </div>
  <div class="recipient">
    <span class="recipient-name">JOHN SMITH</span>
    Street Name,City Name.<br>Zip Coad 0000
  </div>
  <div class="body-copy">
    <p>Lorem Ipsum is simply dummy text of the printing and typesetting industry. Lorem Ipsum has been the industry's standard dummy text ever since the 1500s, when an unknown printer took a galley of type and scrambled it to make a type specimen book. It has survived not only five centuries, but also the leap into electronic typesetting, remaining essentially unchanged. It was popularised in the 1960s with the release of Letraset sheets containing Lorem Ipsum passages, and more recently with desktop publishing software like Aldus PageMaker including versions of Lorem Ipsum.</p>
    <p>It is a long established fact that a reader will be distracted by the readable content of a page when looking at its layout. The point of using Lorem Ipsum is that it has a more-or-less normal distribution of letters, as opposed to using 'Content here, content here', making it look like readable English. Many desktop publishing packages and web page editors now use Lorem Ipsum as their default model text, and a search for 'lorem ipsum' will uncover many web sites still in their infancy. Various versions have evolved over the years, sometimes by accident, sometimes on purpose (injected humour and the like).</p>
  </div>
  <div class="closing">Regards,</div>
  <div class="signature" role="img" aria-label="Handwritten signature of John Doe"></div>
  <div class="signoff"><span class="signer">John Doe</span><br>General Maneger</div>
  <svg class="bands" viewBox="0 0 622 90" preserveAspectRatio="none" aria-hidden="true">
    <polygon points="0,22 0,46 232,68" fill="var(--yellow)"/>
    <polygon points="622,0 622,32 232,68" fill="var(--red)"/>
    <polygon points="0,52 232,72 622,39 622,90 0,90" fill="var(--slate)"/>
  </svg>
</section>

<section class="sheet folder" aria-label="Presentation folder">
  <div class="folder-spine"></div>
  <div class="brand on-dark">
    <span class="brand-square"></span><span class="brand-rule"></span>
    <span class="brand-name">Bayline<br>Blinds</span>
  </div>
  <div class="folder-url">www.yourcompany.com</div>
</section>

<section class="sheet card-front" aria-label="Business card front">
  <div class="brand small">
    <span class="brand-square"></span><span class="brand-rule"></span>
    <span class="brand-name">Bayline<br>Blinds</span>
  </div>
  <div class="card-divider"></div>
  <div class="card-details">
    <div class="person">Jhone Smith</div>
    <div class="role">Principal</div>
    <div class="addr">0000 Youe Address,2nd Ste.<br>Harbourton, Westland 1234</div>
    <div><span class="icon"></span>000 000 0000</div>
    <div><span class="icon"></span>000 000 0000</div>
    <div><span class="icon"></span>yourcompany@gmail.com</div>
  </div>
  <svg class="bands" viewBox="0 0 430 50" preserveAspectRatio="none" aria-hidden="true">
    <polygon points="0,10 0,26 175,45" fill="var(--yellow)"/>
    <polygon points="430,0 430,18 175,45" fill="var(--red)"/>
    <polygon points="0,32 175,48 430,24 430,50 0,50" fill="var(--slate)"/>
  </svg>
</section>

<section class="sheet card-back" aria-label="Business card back">
  <div class="brand small on-dark">
    <span class="brand-square"></span><span class="brand-rule"></span>
    <span class="brand-name">Bayline<br>Blinds</span>
  </div>
  <div class="card-url">www.yourcompany.com</div>
</section>

</body>
</html>
```